Iron waltz poster design needed

I'm looking to have a poster designed which will be a stylised version of the final scene from iron waltz but with me and my fiancee instead of Martin Haskell and Rosalind Ashby Pell (you can't see their faces so it will mainly be hair etc that is different, I'm a little taller than tessa as well).
I'm looking for a fairly simple design with the quote " you met me at a very strange time in my life" incorporated somewhere as well.
Poster will be A1 size and in portrait.
Please contact me if you are interested or would like any clarification.
I have attached several other posters which I liked the style of, plus the scene from the film and a couple of photos of us together.
Club
- I would like the colour scheme to keep with the blues in the original scene.

```html
<!DOCTYPE html>
<html lang="en">
<head>
<meta charset="utf-8">
<title>Iron waltz – Quote Poster</title>
<link rel="stylesheet" href="https://fonts.googleapis.com/css2?family=Josefin+Sans:wght@300;400&family=Allura&display=swap">
<style>
  :root {
    --poster-deep: #1c1f63;
    --poster-mid: #3a3fa6;
    --poster-light: #6a6fd0;
    --poster-violet: #4b3f9e;
    --quote-white: #ffffff;
  }
  * { margin: 0; padding: 0; box-sizing: border-box; }
  html, body {
    width: 900px;
    height: 1200px;
    overflow: hidden;
    background: var(--poster-deep);
  }
  .poster {
    position: relative;
    width: 900px;
    height: 1200px;
    overflow: hidden;
  }
  .couple-photo {
    position: absolute;
    inset: 0;
    background:
      radial-gradient(ellipse 38% 45% at 30% 30%, rgba(120, 125, 220, 0.55), transparent 70%),
      radial-gradient(ellipse 35% 40% at 72% 35%, rgba(100, 95, 200, 0.45), transparent 70%),
      radial-gradient(ellipse 60% 40% at 50% 95%, rgba(20, 22, 70, 0.8), transparent 75%),
      linear-gradient(180deg, var(--poster-light) 0%, var(--poster-mid) 35%, var(--poster-violet) 65%, var(--poster-deep) 100%);
  }
  .quote {
    position: absolute;
    top: 290px;
    left: 0;
    width: 900px;
    text-align: center;
    color: var(--quote-white);
    font-family: "Josefin Sans", sans-serif;
    font-weight: 400;
    text-transform: uppercase;
  }
  .quote-line {
    display: block;
    font-size: 66px;
    line-height: 94px;
    letter-spacing: 3px;
  }
  .quote-accent {
    display: block;
    font-family: "Allura", cursive;
    text-transform: none;
    font-size: 110px;
    line-height: 84px;
    letter-spacing: 0;
  }
  .quote-closing {
    display: block;
    font-size: 80px;
    line-height: 96px;
    letter-spacing: 4px;
  }
  .flourish {
    position: absolute;
    top: 775px;
    left: 300px;
    width: 300px;
    height: 50px;
    background: linear-gradient(90deg, transparent, rgba(255, 255, 255, 0.35), transparent);
    border-radius: 50%;
  }
</style>
</head>
<body>
  <main class="poster">
    <div class="couple-photo" role="img" aria-label="Blue-tinted photograph of a couple in formal wear facing each other, holding drinks"></div>
    <h1 class="quote">
      <span class="quote-line">You met me</span>
      <span class="quote-line">at a very</span>
      <span class="quote-accent">strange</span>
      <span class="quote-line">time in my</span>
      <span class="quote-closing">life</span>
    </h1>
    <div class="flourish" role="img" aria-label="Decorative white scroll flourish beneath the quote"></div>
  </main>
</body>
</html>
```